Harlow Grading and Septic needs a flyer to submit to contractors to offer our services

I need a sleek profession one page full color high gloss document showcasing our services to give to Mobile Home Companies and contractors that need our services.

Home Builders. Mobile Home Salesmen. People Building new homes.

Construction

Serif
Sans Serif

• Phone Number. Email address. Logo. Services offered: Mobile Home Pads, Meter Pole Placement and Connection, Waterline Connection, On Site Septic System Installs
• Jokes, Nothing trying to be cute

```html
<!DOCTYPE html>
<html lang="en">
<head>
<meta charset="UTF-8">
<title>Harlow Grading and Septic – Professional Wastewater Management</title>
<link href="https://fonts.googleapis.com/css2?family=Oswald:wght@500;700&family=Open+Sans:wght@400;600;700&display=swap" rel="stylesheet">
<style>
  :root{
    --red:#b71c22;
    --red-dark:#7a0f13;
    --navy:#142c5f;
    --blue:#1f58b0;
    --blue-light:#2f6fd0;
    --white:#ffffff;
    --ink:#2a2a2a;
    --muted:#5b6270;
  }
  *{margin:0;padding:0;box-sizing:border-box}
  html,body{width:900px;height:1200px;overflow:hidden;background:#fff}
  .flyer{position:relative;width:900px;height:1200px;background:var(--white);font-family:"Open Sans",sans-serif;color:var(--ink);overflow:hidden}

  /* header */
  .header-bg{position:absolute;left:0;top:0;width:900px;height:350px}
  .brand{position:absolute;right:40px;top:28px;display:flex;align-items:center;gap:10px;
    font-family:"Oswald",sans-serif;font-weight:700;font-size:22px;color:var(--navy);text-transform:uppercase;letter-spacing:.5px}
  .brand-mark{width:18px;height:18px;background:var(--red);border-radius:50%}
  .headline{position:absolute;left:44px;top:70px;width:520px;color:var(--white)}
  .headline h1{font-family:"Oswald",sans-serif;font-weight:700;font-size:66px;line-height:1;text-transform:uppercase;letter-spacing:1px}
  .headline h2{font-family:"Oswald",sans-serif;font-weight:500;font-size:27px;text-transform:uppercase;letter-spacing:1.5px;margin-top:6px}
  .headline p{font-size:14px;line-height:1.5;margin-top:14px;width:440px;opacity:.95}
  .cta{position:absolute;left:44px;top:274px;background:var(--white);color:var(--red);
    font-family:"Oswald",sans-serif;font-weight:700;font-size:22px;padding:7px 18px;text-transform:uppercase;letter-spacing:.5px}

  /* services column */
  .services{position:absolute;left:0;top:350px;width:440px;height:800px;background:var(--navy);padding:0 36px 0 40px}
  .section-band{font-family:"Oswald",sans-serif;font-weight:700;font-size:28px;text-transform:uppercase;letter-spacing:1px;color:var(--white)}
  .services .section-band{background:var(--blue);margin:28px -36px 30px -40px;padding:8px 40px}
  .service{display:flex;gap:18px;margin-bottom:38px}
  .service svg{flex:0 0 56px}
  .service h3{font-family:"Oswald",sans-serif;font-weight:500;font-size:21px;color:var(--white);text-transform:uppercase;letter-spacing:.5px}
  .service p{font-size:14px;line-height:1.55;color:#c9d4ea;margin-top:4px}

  /* about column */
  .about{position:absolute;left:470px;top:350px;width:394px}
  .about h2{font-family:"Oswald",sans-serif;font-weight:700;font-size:30px;color:var(--navy);text-transform:uppercase;letter-spacing:1px;margin-top:30px;
    padding-bottom:6px;border-bottom:4px solid var(--red);display:inline-block}
  .about p{font-size:13.5px;line-height:1.6;color:var(--muted);margin-top:16px}
  .photo{display:block}
  .photo-wide{width:394px;height:180px;margin-top:20px;background:linear-gradient(160deg,#a9bdd1,#7f8a80 60%,#5f6b4a)}
  .photo-row{display:flex;gap:14px;margin-top:14px}
  .photo-half{width:190px;height:140px}
  .photo-a{background:linear-gradient(170deg,#9fb7cc,#8c7a5e 65%,#6d5a40)}
  .photo-b{background:linear-gradient(170deg,#b2c3d4,#7b8f5a 60%,#5c6e3c)}
  .contact{margin-top:22px}
  .contact-line{display:flex;align-items:center;gap:12px;font-family:"Oswald",sans-serif;font-weight:500;font-size:22px;color:var(--navy);margin-bottom:8px}
  .contact-line.small{font-family:"Open Sans",sans-serif;font-weight:600;font-size:15px}
  .icon-dot{width:32px;height:32px;border-radius:50%;background:var(--red);display:flex;align-items:center;justify-content:center}

  .footer-band{position:absolute;left:0;bottom:0;width:900px;height:50px;background:linear-gradient(90deg,var(--red-dark),var(--red))}
</style>
</head>
<body>
<div class="flyer">

  <svg class="header-bg" viewBox="0 0 900 350" aria-hidden="true">
    <defs>
      <linearGradient id="redGrad" x1="0" y1="0" x2="1" y2="1">
        <stop offset="0" stop-color="#d3262c"/>
        <stop offset="1" stop-color="#7a0f13"/>
      </linearGradient>
      <linearGradient id="siteGrad" x1="0" y1="0" x2="0" y2="1">
        <stop offset="0" stop-color="#a9c2dc"/>
        <stop offset=".55" stop-color="#d9d6cc"/>
        <stop offset="1" stop-color="#6f7f4f"/>
      </linearGradient>
    </defs>
    <polygon points="0,0 640,0 520,350 0,350" fill="url(#redGrad)"/>
    <g role="img" aria-label="Photo of a finished mobile home set on a prepared pad">
      <polygon points="600,100 900,100 900,350 520,350" fill="url(#siteGrad)"/>
    </g>
    <polygon points="640,0 660,0 540,350 520,350" fill="#ffffff"/>
  </svg>

  <div class="brand"><span class="brand-mark"></span>Harlow Grading and Septic</div>

  <div class="headline">
    <h1>Professional</h1>
    <h2>Wastewater Management</h2>
    <p>Harlow Grading and Septic offers dependable site work and septic installation for builders, dealers and new homeowners across the region.</p>
  </div>
  <div class="cta">Call us now for a free estimate!</div>

  <section class="services">
    <div class="section-band">Our Service</div>

    <div class="service">
      <svg width="56" height="62" viewBox="0 0 56 62" aria-hidden="true"><polygon points="28,2 54,16 54,46 28,60 2,46 2,16" fill="#b71c22"/><path d="M16 31 l8 8 l16 -16" stroke="#fff" stroke-width="4" fill="none" stroke-linecap="round" stroke-linejoin="round"/></svg>
      <div><h3>Mobile Home Pads</h3><p>Level, compacted gravel pads prepared to dealer and county specifications for every home size.</p></div>
    </div>
    <div class="service">
      <svg width="56" height="62" viewBox="0 0 56 62" aria-hidden="true"><polygon points="28,2 54,16 54,46 28,60 2,46 2,16" fill="#b71c22"/><path d="M16 31 l8 8 l16 -16" stroke="#fff" stroke-width="4" fill="none" stroke-linecap="round" stroke-linejoin="round"/></svg>
      <div><h3>Meter Pole Placement and Connection</h3><p>We set meter poles and run service connections ready for utility inspection and hookup.</p></div>
    </div>
    <div class="service">
      <svg width="56" height="62" viewBox="0 0 56 62" aria-hidden="true"><polygon points="28,2 54,16 54,46 28,60 2,46 2,16" fill="#b71c22"/><path d="M16 31 l8 8 l16 -16" stroke="#fff" stroke-width="4" fill="none" stroke-linecap="round" stroke-linejoin="round"/></svg>
      <div><h3>Waterline Connection</h3><p>Trenching and waterline installation from the meter or well straight to your home.</p></div>
    </div>
    <div class="service">
      <svg width="56" height="62" viewBox="0 0 56 62" aria-hidden="true"><polygon points="28,2 54,16 54,46 28,60 2,46 2,16" fill="#b71c22"/><path d="M16 31 l8 8 l16 -16" stroke="#fff" stroke-width="4" fill="none" stroke-linecap="round" stroke-linejoin="round"/></svg>
      <div><h3>On Site Septic System Installs</h3><p>Permitted conventional and engineered septic systems designed, installed and inspected on schedule.</p></div>
    </div>
  </section>

  <section class="about">
    <h2>About Us</h2>
    <p>Harlow Grading and Septic is a family owned contractor serving home builders, mobile home dealers and property owners. Our crews bring modern equipment and years of field experience to every job, from the first cut of the pad to the final septic inspection. We show up on time, keep sites clean and finish work that passes the first time.</p>
    <div class="photo photo-wide" role="img" aria-label="Photo of a septic tank being set into an excavated site"></div>
    <div class="photo-row">
      <div class="photo photo-half photo-a" role="img" aria-label="Photo of an excavator trenching for a waterline"></div>
      <div class="photo photo-half photo-b" role="img" aria-label="Photo of a graded septic drain field"></div>
    </div>
    <div class="contact">
      <div class="contact-line">
        <span class="icon-dot"><svg width="16" height="16" viewBox="0 0 24 24" aria-hidden="true"><path d="M6.6 10.8a15.2 15.2 0 0 0 6.6 6.6l2.2-2.2a1 1 0 0 1 1-.25 11.4 11.4 0 0 0 3.6.57 1 1 0 0 1 1 1V20a1 1 0 0 1-1 1A17 17 0 0 1 3 4a1 1 0 0 1 1-1h3.5a1 1 0 0 1 1 1c0 1.25.2 2.45.57 3.57a1 1 0 0 1-.25 1z" fill="#fff"/></svg></span>
        (555) 014-2290
      </div>
      <div class="contact-line small">
        <span class="icon-dot"><svg width="16" height="16" viewBox="0 0 24 24" aria-hidden="true"><rect x="3" y="5" width="18" height="14" rx="2" fill="#fff"/><path d="M3 6l9 7 9-7" stroke="#b71c22" stroke-width="2" fill="none"/></svg></span>
        office@harlowgrading.com
      </div>
    </div>
  </section>

  <div class="footer-band"></div>
</div>
</body>
</html>
```